Post Card Design Bright Lantern Youth

We need a postcard design that will be mailed to all residents offering free pickups of donated clothing. Our foundation is called Bright Lantern Youth, we are a nonprofit charitable organization that provides meals and medical services to children in need in Honduras. Collecting unwanted second-hand clothing generates revenue that helps fund the mission and programs run by our foundation. We would like to offer our pickup services to everyone who has any unwanted reusable clothing.

```html
<!DOCTYPE html>
<html lang="en">
<head>
<meta charset="utf-8">
<title>Bright Lantern Youth – Free Clothing Pickups Postcard</title>
<link href="https://fonts.googleapis.com/css2?family=Poppins:wght@400;500;600;700;800&display=swap" rel="stylesheet">
<style>
  :root{
    --green:#7dc22e;
    --teal:#2aa89a;
    --blue:#0c8fd9;
    --orange:#f7a51c;
    --pink:#ec2a7a;
    --white:#ffffff;
    --stage:#ececec;
    --stamp:#d0d0d0;
  }
  *{margin:0;padding:0;box-sizing:border-box}
  html,body{width:1200px;height:1200px;overflow:hidden}
  body{background:var(--stage);position:relative;font-family:"Poppins",sans-serif;color:var(--white)}

  .postcard{position:absolute;width:819px;height:592px;overflow:hidden}
  .postcard--back{left:348px;top:574px;background:var(--white)}
  .postcard--front{left:29px;top:25px;background:var(--white)}

  /* back */
  .back-panel{position:absolute;left:0;top:0;width:510px;height:592px;
    background:linear-gradient(180deg,var(--green) 0%,var(--teal) 50%,var(--blue) 100%)}
  .back-heading{position:absolute;left:38px;top:50px;font-size:35px;font-weight:600;line-height:40px;letter-spacing:-.3px}
  .back-body{position:absolute;left:38px;top:138px;width:450px;font-size:16.5px;line-height:26px;font-weight:400}
  .help-title{position:absolute;left:0;width:510px;top:300px;text-align:center;font-size:20px;font-weight:700;letter-spacing:-.3px}
  .step{position:absolute;top:336px;width:138px;text-align:center;font-size:14px;line-height:19.5px}
  .step__badge{width:90px;height:90px;margin:0 auto 14px;border-radius:44% 56% 50% 50%;
    border:3px solid var(--white);background:linear-gradient(180deg,var(--blue),var(--green) 75%);
    display:flex;align-items:center;justify-content:center}
  .step--gather{left:39px}.step--call{left:197px}.step--relax{left:339px}
  .contact-row{position:absolute;display:flex;align-items:center;gap:26px}
  .contact-row--back{left:24px;top:530px}
  .phone{display:flex;align-items:center;gap:8px;font-size:32px;font-weight:700;letter-spacing:-.5px;white-space:nowrap}
  .links{font-size:12px;line-height:16.5px;white-space:nowrap}
  .links div{display:flex;align-items:center;gap:8px}
  .stamp-box{position:absolute;left:702px;background:var(--stamp);width:111px}
  .stamp-box--a{top:4px;height:48px}.stamp-box--b{top:55px;height:34px}

  /* front */
  .front-art{position:absolute;inset:0}
  .front-title{position:absolute;left:51px;top:50px;font-size:45px;font-weight:600;letter-spacing:-.5px;line-height:56px}
  .front-sub{position:absolute;left:53px;top:119px;font-size:21.5px;line-height:30.3px;font-weight:400}
  .brand{position:absolute;left:640px;top:20px;width:170px;display:flex;flex-direction:column;align-items:center;gap:8px;
    color:var(--green);font-size:17px;font-weight:700;text-align:center;line-height:20px}
  .brand__dot{width:44px;height:44px;border-radius:50%;background:var(--green)}
  .callout{position:absolute;left:218px;top:306px;width:210px;text-align:center;font-size:24px;font-weight:800;line-height:27px;letter-spacing:-.5px;text-transform:uppercase}
  .front-bar{position:absolute;left:0;bottom:0;width:819px;height:72px;background:linear-gradient(180deg,#151515,#2b2b2b)}
  .contact-row--front{left:283px;top:538px}
</style>
</head>
<body>

<section class="postcard postcard--back" aria-label="Postcard back">
  <div class="back-panel">
    <h2 class="back-heading">Join us in supporting<br>children in Honduras</h2>
    <p class="back-body">Bright Lantern Youth is a nonprofit organization dedicated to providing meals and medical services to children in need. By donating your gently used clothing, you are directly helping to fund our programs and changing lives for the better.</p>
    <h3 class="help-title">IT'S EASY TO HELP:</h3>

    <div class="step step--gather">
      <div class="step__badge">
        <svg width="44" height="40" viewBox="0 0 44 40" aria-hidden="true"><path d="M14 6 L22 10 L30 6 L40 14 L35 21 L31 18 V36 H13 V18 L9 21 L4 14 Z" fill="#fff"/></svg>
      </div>
      Simply gather your<br>unwanted, reusable<br>clothing.
    </div>
    <div class="step step--call">
      <div class="step__badge">
        <svg width="44" height="44" viewBox="0 0 44 44" aria-hidden="true"><path d="M10 8c2-2 5-2 6 1l2 6c1 2 0 3-2 4l-2 1c2 5 5 8 10 10l1-2c1-2 2-3 4-2l6 2c3 1 3 4 1 6l-3 3c-10 2-25-13-23-23z" fill="#fff"/><circle cx="32" cy="11" r="6" fill="#fff"/></svg>
      </div>
      Call or visit us<br>online to schedule<br>a free pickup.
    </div>
    <div class="step step--relax">
      <div class="step__badge">
        <svg width="48" height="44" viewBox="0 0 48 44" aria-hidden="true"><path d="M24 16c-3-3-9-6-9-11 0-3 3-5 5-4 2 0 3 2 4 3 1-1 2-3 4-3 2-1 5 1 5 4 0 5-6 8-9 11z" fill="#fff"/><path d="M6 16v12l10 10h6V30l-8-8M42 16v12L32 38h-6V30l8-8" fill="none" stroke="#fff" stroke-width="3.5" stroke-linejoin="round"/></svg>
      </div>
      We'll take<br>care of the rest!
    </div>

    <div class="contact-row contact-row--back">
      <div class="phone">
        <svg width="22" height="22" viewBox="0 0 24 24" aria-hidden="true"><path d="M5 2c1-1 3-1 4 1l2 4c0 1 0 2-1 3l-1 1c1 3 3 5 6 6l1-1c1-1 2-1 3-1l4 2c2 1 2 3 1 4l-2 2C14 24 0 10 3 4z" fill="#fff"/></svg>
        000 000 1234
      </div>
      <div class="links">
        <div><svg width="12" height="10" viewBox="0 0 12 10" aria-hidden="true"><rect x=".5" y=".5" width="11" height="9" fill="none" stroke="#fff"/><path d="M.5.5 6 5l5.5-4.5" fill="none" stroke="#fff"/></svg>email@yourcompanyname.com</div>
        <div><svg width="12" height="12" viewBox="0 0 12 12" aria-hidden="true"><circle cx="6" cy="6" r="5.5" fill="none" stroke="#fff"/><path d="M.5 6h11M6 .5c-3 3-3 8 0 11M6 .5c3 3 3 8 0 11" fill="none" stroke="#fff"/></svg>www.yourwebsite.com</div>
      </div>
    </div>
  </div>
  <div class="stamp-box stamp-box--a"></div>
  <div class="stamp-box stamp-box--b"></div>
</section>

<section class="postcard postcard--front" aria-label="Postcard front">
  <svg class="front-art" width="819" height="592" viewBox="0 0 819 592">
    <defs>
      <linearGradient id="skyGrad" x1="0" y1="0" x2="0" y2="1">
        <stop offset="0" stop-color="#7dc22e"/><stop offset=".5" stop-color="#2aa89a"/><stop offset="1" stop-color="#0c8fd9"/>
      </linearGradient>
      <linearGradient id="bandGrad" x1="0" y1="0" x2="1" y2="0">
        <stop offset="0" stop-color="#fdc21a"/><stop offset="1" stop-color="#f26a2a"/>
      </linearGradient>
      <linearGradient id="calloutGrad" x1="0" y1="0" x2="0" y2="1">
        <stop offset="0" stop-color="#0c8fd9"/><stop offset=".6" stop-color="#5bb53a"/><stop offset="1" stop-color="#7dc22e"/>
      </linearGradient>
      <linearGradient id="dressGrad" x1="0" y1="0" x2="1" y2="1">
        <stop offset="0" stop-color="#f2b3a6"/><stop offset=".5" stop-color="#b9c0dc"/><stop offset="1" stop-color="#e9a797"/>
      </linearGradient>
      <linearGradient id="rackGrad" x1="0" y1="0" x2="1" y2="0">
        <stop offset="0" stop-color="#c7ab8c"/><stop offset=".45" stop-color="#e8e2d8"/><stop offset=".7" stop-color="#a88a6b"/><stop offset="1" stop-color="#1c1c1c"/>
      </linearGradient>
    </defs>
    <path d="M0 0H819V235C760 215 700 225 640 240C520 250 430 240 330 250C200 262 80 268 0 255Z" fill="url(#skyGrad)"/>
    <path d="M659 0H819V135C790 165 770 190 745 192C700 196 650 160 625 120C600 80 615 30 659 0Z" fill="#fff"/>
    <path d="M0 255C80 268 200 262 330 250C250 282 120 300 0 292Z" fill="url(#bandGrad)"/>
    <path d="M330 250C400 243 470 236 560 230C480 252 420 262 380 268Z" fill="var(--pink)"/>
    <g role="img" aria-label="Photo of a child's light blue party dress with matching bloomers">
      <path d="M0 330C60 305 150 300 200 320C250 345 265 420 245 480C225 545 175 585 120 591H0Z" fill="url(#dressGrad)"/>
    </g>
    <g role="img" aria-label="Photo of children's checked coats and shirts hanging on a store rack">
      <path d="M470 130C540 100 650 110 705 160C750 205 775 290 765 350C755 420 705 465 640 466C570 468 500 440 460 400C425 360 415 300 425 240C433 190 440 145 470 130Z" fill="url(#rackGrad)"/>
    </g>
    <path d="M290 245C340 225 400 245 430 290C460 340 440 410 390 450C345 485 270 480 235 440C200 400 205 330 230 290C245 265 265 253 290 245Z" fill="url(#calloutGrad)" stroke="#fff" stroke-width="4"/>
  </svg>

  <h1 class="front-title">Free Clothing Pickups</h1>
  <p class="front-sub">Your unwanted clothing can help<br>provide meals and medical care<br>for children in need!</p>
  <div class="brand"><span class="brand__dot"></span>Bright Lantern Youth</div>
  <p class="callout">Clear your closet while making a difference!</p>

  <div class="front-bar"></div>
  <div class="contact-row contact-row--front">
    <div class="phone">
      <svg width="22" height="22" viewBox="0 0 24 24" aria-hidden="true"><path d="M5 2c1-1 3-1 4 1l2 4c0 1 0 2-1 3l-1 1c1 3 3 5 6 6l1-1c1-1 2-1 3-1l4 2c2 1 2 3 1 4l-2 2C14 24 0 10 3 4z" fill="#fff"/></svg>
      000 000 1234
    </div>
    <div class="links">
      <div><svg width="12" height="10" viewBox="0 0 12 10" aria-hidden="true"><rect x=".5" y=".5" width="11" height="9" fill="none" stroke="#fff"/><path d="M.5.5 6 5l5.5-4.5" fill="none" stroke="#fff"/></svg>email@yourcompanyname.com</div>
      <div><svg width="12" height="12" viewBox="0 0 12 12" aria-hidden="true"><circle cx="6" cy="6" r="5.5" fill="none" stroke="#fff"/><path d="M.5 6h11M6 .5c-3 3-3 8 0 11M6 .5c3 3 3 8 0 11" fill="none" stroke="#fff"/></svg>www.yourwebsite.com</div>
    </div>
  </div>
</section>

</body>
</html>
```